Postcard needed for expert witness service

Looking for a professional postcard that will be mailed to personal injury lawyers / law firms to introduce my expert witness services.

Target Market(s)

Law firms, personal injury lawyers

Industry/Entity Type

Expert witness, law

Font styles to use
Sans Serif

Requirements
Must have
• Logo: The Frost Counsel [Main Heading]Do you handle snow and ice related slip and falls? Darrel is one of the top snow industry experts in the country! [Following should be in a list type fashion, possibly bulleted]Darrel's credentials: Accredited Winter Practitioner (AWP), past WRTA board member and chair, former ISO 9001 certified snow company owner , 32 years in the industry. (555) 284-3917 NOTES: Postcard will be 4" x 6" Please use both sides however must have room for labels and stamp
Should not have
• Wouldn't suggest using both photos on same side. Honestly, feel free to only use one of the slip and fall photos if it works out better. Thanks!

```html
<!DOCTYPE html>
<html lang="en">
<head>
<meta charset="utf-8">
<title>The Frost Counsel – Postcard</title>
<link href="https://fonts.googleapis.com/css2?family=Montserrat:wght@400;700;800&family=Barlow+Semi+Condensed:wght@500;600&family=Barlow:wght@400;600&display=swap" rel="stylesheet">
<style>
:root{
  --stage:#3d3d3d;
  --ink:#111111;
  --white:#ffffff;
  --band-light:rgba(128,118,110,0.94);
  --band-dark:rgba(104,95,88,0.94);
  --pavement:#8f857c;
  --snow-shadow:#c9c6c3;
  --snow:#eceae7;
  --snow-bright:#f6f5f3;
  --coat:#4a3a34;
  --denim:#4f6477;
  --sky:#f1f1f0;
  --haze:#dedfe0;
  --facade:#6f8096;
  --facade-warm:#8a5f4c;
  --wet-pave:#8c8f94;
  --wet-pave-dark:#676a70;
  --stamp-line:#cfcfcf;
}
*{margin:0;padding:0;box-sizing:border-box}
html,body{width:1200px;height:904px;overflow:hidden;background:var(--stage)}
.stage{position:relative;width:1200px;height:904px}
.postcard{position:absolute;width:493px;height:329px;overflow:hidden;background:var(--white)}
.postcard--front{left:215px;top:98px}
.postcard--back{left:492px;top:478px}
.photo{position:absolute;inset:0}
.photo--front{
  background:
    radial-gradient(ellipse 30% 34% at 62% 62%, rgba(79,100,119,0.85) 0%, rgba(79,100,119,0.5) 55%, rgba(79,100,119,0) 100%),
    radial-gradient(ellipse 24% 26% at 52% 48%, rgba(74,58,52,0.9) 0%, rgba(74,58,52,0.5) 60%, rgba(74,58,52,0) 100%),
    linear-gradient(118deg, var(--pavement) 0%, var(--pavement) 38%, rgba(143,133,124,0) 58%),
    linear-gradient(200deg, var(--snow-bright) 0%, var(--snow) 40%, var(--snow-shadow) 75%, var(--snow) 100%);
}
.photo--back{
  background:
    radial-gradient(ellipse 22% 40% at 33% 50%, rgba(79,100,119,0.8) 0%, rgba(79,100,119,0.45) 60%, rgba(79,100,119,0) 100%),
    radial-gradient(ellipse 20% 14% at 64% 74%, rgba(150,152,156,0.9) 0%, rgba(150,152,156,0) 100%),
    linear-gradient(90deg, var(--facade-warm) 0%, var(--facade) 9%, rgba(111,128,150,0.6) 20%, rgba(111,128,150,0) 32%),
    linear-gradient(180deg, var(--sky) 0%, var(--haze) 62%, var(--wet-pave) 70%, var(--wet-pave-dark) 100%);
}
.band{position:absolute;left:0}
.band--headline{top:0;width:330px;height:99px;
  background:linear-gradient(90deg,var(--band-light) 0%,var(--band-light) 80%,rgba(128,118,110,0) 100%)}
.band--sub{top:99px;width:345px;height:45px;
  background:linear-gradient(90deg,var(--band-dark) 0%,var(--band-dark) 80%,rgba(104,95,88,0) 100%)}
.headline{position:absolute;left:20px;top:15px;width:270px;
  font-family:"Montserrat",sans-serif;font-weight:800;font-size:23px;line-height:25px;color:var(--white)}
.subhead{position:absolute;left:20px;top:103px;width:260px;
  font-family:"Barlow Semi Condensed",sans-serif;font-weight:600;font-size:14.6px;line-height:18px;color:var(--white)}
.wordmark{position:absolute;font-family:"Montserrat",sans-serif;font-weight:400;color:var(--ink);
  text-transform:uppercase;text-align:center}
.wordmark__line{display:block}
.postcard--front .wordmark{left:312px;top:18px;width:168px;font-size:21px;line-height:22px;letter-spacing:0.5px}
.postcard--back .wordmark{left:262px;top:28px;width:130px;font-size:16px;line-height:17px;letter-spacing:0.4px}
.credentials{position:absolute;left:20px;top:166px;width:140px;font-family:"Barlow",sans-serif;color:var(--ink)}
.credentials__title{font-weight:600;font-size:10.6px;line-height:13px;margin-bottom:2px}
.credentials__list{list-style:none}
.credentials__item{position:relative;padding-left:13px;font-size:9.8px;line-height:12.4px;margin-bottom:2.4px}
.credentials__item svg{position:absolute;left:0;top:2.2px;width:8px;height:8px}
.call-bar{position:absolute;left:0;top:292px;display:flex;align-items:center;gap:7px;height:24px;padding:0 11px 0 20px;
  background:var(--ink);border-radius:0 12px 12px 0;color:var(--white);
  font-family:"Montserrat",sans-serif;font-weight:700;font-size:11px;white-space:nowrap}
.call-bar svg{width:14px;height:14px}
.stamp-box{position:absolute;left:419px;top:20px;width:53px;height:49px;border:1.5px solid var(--stamp-line)}
</style>
</head>
<body>
<div class="stage">

  <section class="postcard postcard--front">
    <div class="photo photo--front" role="img" aria-label="Photo of a woman in a brown winter coat and knit hat falling on an icy, snowy sidewalk"></div>
    <div class="band band--headline"></div>
    <div class="band band--sub"></div>
    <h1 class="headline">Do you handle snow and ice related slip and falls?</h1>
    <p class="subhead">Darrel is one of the top snow industry experts in the country!</p>
    <div class="wordmark"><span class="wordmark__line">The Frost</span><span class="wordmark__line">Counsel</span></div>
    <div class="credentials">
      <p class="credentials__title">Darrel's credentials:</p>
      <ul class="credentials__list">
        <li class="credentials__item"><svg viewBox="0 0 10 10"><circle cx="5" cy="5" r="5" fill="#111"/><path d="M2.8 5.1l1.5 1.5 3-3.1" fill="none" stroke="#fff" stroke-width="1.3"/></svg>Accredited Winter Practitioner (AWP)</li>
        <li class="credentials__item"><svg viewBox="0 0 10 10"><circle cx="5" cy="5" r="5" fill="#111"/><path d="M2.8 5.1l1.5 1.5 3-3.1" fill="none" stroke="#fff" stroke-width="1.3"/></svg>Past WRTA board member and chair</li>
        <li class="credentials__item"><svg viewBox="0 0 10 10"><circle cx="5" cy="5" r="5" fill="#111"/><path d="M2.8 5.1l1.5 1.5 3-3.1" fill="none" stroke="#fff" stroke-width="1.3"/></svg>Former ISO 9001 certified snow company owner</li>
        <li class="credentials__item"><svg viewBox="0 0 10 10"><circle cx="5" cy="5" r="5" fill="#111"/><path d="M2.8 5.1l1.5 1.5 3-3.1" fill="none" stroke="#fff" stroke-width="1.3"/></svg>32 years in the industry</li>
      </ul>
    </div>
    <div class="call-bar">
      <span>CALL US</span>
      <svg viewBox="0 0 16 16"><circle cx="8" cy="8" r="7.5" fill="#fff"/><path d="M5.3 4.2l1.4-.3.8 2-1 .8a5 5 0 0 0 2.8 2.8l.8-1 2 .8-.3 1.4c-.1.4-.5.6-.9.6A6.5 6.5 0 0 1 4.6 5.1c0-.4.3-.8.7-.9z" fill="#111"/></svg>
      <span>(555) 284-3917</span>
    </div>
  </section>

  <section class="postcard postcard--back">
    <div class="photo photo--back" role="img" aria-label="Photo of a man slipping on an icy city sidewalk beside a storefront, his backpack on the ground"></div>
    <div class="wordmark"><span class="wordmark__line">The Frost</span><span class="wordmark__line">Counsel</span></div>
    <div class="stamp-box"></div>
    <div class="call-bar">
      <span>CALL US</span>
      <svg viewBox="0 0 16 16"><circle cx="8" cy="8" r="7.5" fill="#fff"/><path d="M5.3 4.2l1.4-.3.8 2-1 .8a5 5 0 0 0 2.8 2.8l.8-1 2 .8-.3 1.4c-.1.4-.5.6-.9.6A6.5 6.5 0 0 1 4.6 5.1c0-.4.3-.8.7-.9z" fill="#111"/></svg>
      <span>(555) 284-3917</span>
    </div>
  </section>

</div>
</body>
</html>
```